Etiketten für Getränkehersteller- und händler
Zielgruppe
Wir sind Getränkehersteller- und händler. Für unsere Partner haben wir exklusive Eigenmarken, die nur unserer Partner verkaufen. Der Sonnenrebe ist eine exklusive Gastronomiemarke, die nicht im Handel erhältlich ist. Leichter, gut-trinkbarer, mainstreamiger Sommerwein, für jede Art von Gastronomie. Den Wein gibt es im 3. Jahr.
Wir planen für die Zukunft, neben dem Weißwein die Produktrange um einen Rot-und Roséwein zu erweitern.
Aufgabenstellung
Arbeiten mit dem Logo/Etikett
1) Sonnenrebe-Schriftzug ist angemeldete Wort-Bild-Marke
2) Sonnenrebe soll weiterhin nummeriert werden (nächster Wein #4 Weisswein,)
3) Liquit steht erst zu einem späteren Zeitpunkt fest und kann daher beliebig für den Entwurf ausgewählt werden.
4) Darstellung des Etiketts auf der Flasche (siehe Anhang)
Was wir uns wünschen:
Alternative 1: Weiterentwicklung der Etiketten
1) Layout der Etiketten auf bestehender Designvorlage (weißwein, Rotwein, Rosé) mit neuem Farbcode weiterentwickeln
2) Etikettendesigns für die Sonnenreben #4 (2018), #5 (2019), #6 (2020)
Alternative 2: Modifizierung der Etiketten
1) Weiterentwicklung des bestehenden Etikettendesigns mit einem hohen Wiedererkennungswert zum heutigen Design
2) Anpassung des Logos in anderen Farben möglich, aber nicht zwingen
3) mehrere Ideen-Vorschläge gerne gesehen, muss aber nur für die 3 Sorten für das Jahr 2019 aufgezeigt werden
Farbgestaltung
1) Rotwein in rötlichen Tönen, gedeckte eher winterliche Farben
2) Rosé in rosa-Nuancen, helle Farben
3) Weißwein in hellen Sommerfarben (gelb,orange, sommerlich)
Infos zu Etikettenqualität und Flasche
Papier: Klebeetikett mit gestrichenem Papier
Flasche: Klarglasflasche für Weiß/Roséwein; Grün/Braunglas für Rotwein

```html
<!DOCTYPE html>
<html lang="de">
<head>
<meta charset="utf-8">
<title>Sonnenrebe Etiketten #4 #5 #6</title>
<link href="https://fonts.googleapis.com/css2?family=Antonio:wght@400;600;700&display=swap" rel="stylesheet">
<style>
  :root {
    --bg: #ffffff;
    --ink: #5d5d5d;
    --green: #5cb800;
    --green-light: #a8d978;
    --green-pale: #d6ebc2;
    --paper: #ffffff;
  }
  * { box-sizing: border-box; margin: 0; padding: 0; }
  html, body { width: 1200px; height: 960px; overflow: hidden; background: var(--bg); }
  .label-row {
    position: absolute; left: 30px; top: 267px;
    display: flex; gap: 60px;
  }
  .label {
    position: relative; width: 340px; height: 425px;
    font-family: "Antonio", "Oswald", sans-serif;
    outline: 1px solid rgba(0,0,0,0.06);
  }
  .label--weiss { --accent:#f5b800; --tint-mid:#ffd97a; --tint-pale:#fdefc4; --divider:#d6bf8e; }
  .label--rose  { --accent:#f0706e; --tint-mid:#f9a8b0; --tint-pale:#fcdde0; --divider:#c8a7a8; }
  .label--lila  { --accent:#c055c8; --tint-mid:#d79be0; --tint-pale:#eed6ef; --divider:#b89bb8; }

  .pattern-field {
    position: absolute; inset: 0;
    background: linear-gradient(180deg,
      var(--tint-pale) 0%,
      var(--green-pale) 25%,
      var(--green-light) 50%,
      var(--tint-mid) 75%,
      var(--tint-pale) 100%);
  }

  .panel {
    position: absolute; left: 55px; top: 0; width: 124px; height: 100%;
    background: var(--paper);
    border-left: 3px solid var(--divider);
    border-right: 3px solid var(--divider);
  }
  .brand {
    position: absolute; left: 0; right: 0; top: 30px;
    text-align: center;
    color: var(--ink); font-weight: 700;
    font-size: 24px; line-height: 1;
    text-transform: uppercase;
  }
  .edition {
    position: absolute; left: 0; right: 0; top: 66px;
    text-align: center;
    color: var(--ink); font-weight: 700; font-size: 24px; line-height: 1;
  }
  .variety {
    position: absolute; left: 0; right: 0; top: 296px;
    text-align: center; font-weight: 600; line-height: 0.95;
    text-transform: uppercase;
  }
  .variety span { display: block; }
  .variety .maker { color: var(--accent); font-size: 22px; }
  .variety .kind  { color: var(--green); font-size: 29px; }
  .variety .wine  { color: var(--green-light); font-size: 29px; }
  .variety .year  { color: var(--accent); font-size: 36px; }
</style>
</head>
<body>
<main class="label-row">
  <article class="label label--weiss">
    <div class="pattern-field" role="img" aria-label="Horizontales Streifenmuster in Gelb- und Grüntönen"></div>
    <div class="panel">
      <div class="brand">Sonnenrebe</div>
      <div class="edition">#4</div>
      <div class="variety">
        <span class="maker">Muster</span>
        <span class="kind">Weiss</span>
        <span class="wine">Wein</span>
        <span class="year">2018</span>
      </div>
    </div>
  </article>

  <article class="label label--rose">
    <div class="pattern-field" role="img" aria-label="Horizontales Streifenmuster in Rosa- und Grüntönen"></div>
    <div class="panel">
      <div class="brand">Sonnenrebe</div>
      <div class="edition">#5</div>
      <div class="variety">
        <span class="maker">Muster</span>
        <span class="kind">Weiss</span>
        <span class="wine">Wein</span>
        <span class="year">2019</span>
      </div>
    </div>
  </article>

  <article class="label label--lila">
    <div class="pattern-field" role="img" aria-label="Horizontales Streifenmuster in Flieder- und Grüntönen"></div>
    <div class="panel">
      <div class="brand">Sonnenrebe</div>
      <div class="edition">#6</div>
      <div class="variety">
        <span class="maker">Muster</span>
        <span class="kind">Weiss</span>
        <span class="wine">Wein</span>
        <span class="year">2020</span>
      </div>
    </div>
  </article>
</main>
</body>
</html>
```